Tarvel Business Card Design

We need a business card design for a new company in NJ called Tarvel LLC. We provide plumbing, sewer & drain cleaning, and full bath remodeling services. We need a logo design that will be used for several applications such as; cards, stickers, t shirts, and truck lettering. The company hopes to one day be a full service operation offering plumbing, heating, cooling, electric, so we need a design that is very general (aka no pipe wrenches). Colors will be royal blue,neon lime green, and would like to add diamond plate or steel plate to give it a very masculine feel and look.

Contact Information for Business Card

Tarvel LLC. ,Plumbing, Sewer & Drain Cleaning, Bath Remodeling
North Brunswick, NJ 08902
732.555.0148
Tarvelpipeworks.example
Info@tarvelpipeworks.example
Stay calm, ring tarvel!, Rick Movren- President
NJ Master Plumbing License: 58217, Residential & Commercial Service

Requirements
Should not have
• Tool icons
Script font

```html
<!DOCTYPE html>
<html lang="en">
<head>
<meta charset="utf-8">
<title>Tarvel LLC Business Card</title>
<link rel="stylesheet" href="https://fonts.googleapis.com/css2?family=Arimo&family=Cabin:wght@500&family=PT+Sans&display=swap">
<style>
  :root {
    --royal-blue: #0a00e6;
    --lime: #99ff00;
    --ink: #1d1d1d;
    --slogan-grey: #707070;
    --white: #ffffff;
    --frame: #000000;
  }
  * { margin: 0; padding: 0; box-sizing: border-box; }
  html, body { width: 971px; height: 1200px; overflow: hidden; background: var(--white); }
  .canvas { position: relative; width: 971px; height: 1200px; }
  .line { position: absolute; line-height: 1; white-space: nowrap; }

  .card-front {
    position: absolute; left: 0; top: 0; width: 971px; height: 571px;
    border: 2px solid var(--frame); background: var(--white);
  }
  .brand {
    position: absolute; left: 0; width: 100%; top: 212px; text-align: center;
    font-family: "PT Sans", sans-serif; font-size: 74px; line-height: 1;
    color: var(--royal-blue);
  }
  .services-tagline {
    position: absolute; left: 0; width: 100%; top: 330px; text-align: center;
    font-family: "Cabin", sans-serif; font-weight: 500; font-size: 32px; line-height: 1;
    color: var(--ink);
  }
  .tagline-rule {
    position: absolute; left: 202px; top: 362px; width: 567px; height: 2px;
    background: var(--lime);
  }
  .slogan {
    position: absolute; left: 0; width: 100%; top: 457px; text-align: center;
    font-family: "Arimo", sans-serif; font-size: 34px; line-height: 1;
    color: var(--slogan-grey);
  }

  .card-back {
    position: absolute; left: 0; top: 628px; width: 971px; height: 572px;
    background: var(--lime);
    font-family: "Arimo", sans-serif;
  }
  .license { left: 57px; font-size: 20px; color: var(--royal-blue); }
  .license.first { top: 47px; }
  .license.second { top: 74px; }
  .person { right: 52px; text-align: right; color: var(--white); }
  .person-name { top: 44px; font-size: 28px; }
  .person-title { top: 76px; font-size: 20px; letter-spacing: 1px; }
  .company { left: 57px; top: 294px; font-size: 30px; color: var(--ink); }
  .company-services { left: 57px; top: 329px; font-size: 27px; color: var(--ink); }
  .company-location { left: 57px; top: 374px; font-size: 25px; color: var(--ink); letter-spacing: -0.3px; }
  .web { left: 57px; top: 438px; font-size: 25px; color: var(--ink); letter-spacing: -0.3px; }
  .email { left: 57px; top: 476px; font-size: 25px; color: var(--ink); letter-spacing: -0.3px; }
</style>
</head>
<body>
<main class="canvas">
  <section class="card-front">
    <div class="brand">Tarvel LLC</div>
    <div class="services-tagline">Plumbing Sewer &amp; Drain Cleaning Bath</div>
    <div class="tagline-rule"></div>
    <div class="slogan">Stay calm, ring Tarvel!</div>
  </section>

  <section class="card-back">
    <div class="line license first">NJ Master Plumbing License: 58217</div>
    <div class="line license second">Residential &amp; Commercial</div>
    <div class="line person person-name">Rick Movren</div>
    <div class="line person person-title">President</div>
    <div class="line company">Tarvel LLC.</div>
    <div class="line company-services">Plumbing Sewer &amp; Drain Cleaning Bath</div>
    <div class="line company-location">Remodeling North Brunswick, NJ 732.555.0148</div>
    <div class="line web">Website: Tarvelpipeworks.example</div>
    <div class="line email">Email: Info@tarvelpipeworks.example</div>
  </section>
</main>
</body>
</html>
```